SANDWICH SKILLET DESIGN (Packaging)

We require a skillet (sandwich box) designed I have uploaded a similar one we have already
I have uploaded the logo to be placed on the skillet
( BRIGHT MEADOW PANTRY HAWKS LTD)
we would like a sandwich skillet which has a white background and maybe some veg items which maybe found in a sandwich
hope this helps

```html
<!DOCTYPE html>
<html lang="en">
<head>
<meta charset="utf-8">
<title>Bright Meadow Pantry – Sandwich Skillet</title>
<link href="https://fonts.googleapis.com/css2?family=Roboto+Condensed:ital,wght@0,700;1,700&family=Parisienne&family=Cormorant+Garamond:wght@600&display=swap" rel="stylesheet">
<style>
  :root {
    --bg: #e6e6e6;
    --board: #ecebe8;
    --board-edge: #d6d4cf;
    --red: #8e0b0f;
    --white: #ffffff;
    --ink: #1c1c1c;
  }
  * { margin: 0; padding: 0; box-sizing: border-box; }
  html, body { width: 1200px; height: 720px; overflow: hidden; background: var(--bg); }
  .canvas { position: relative; width: 1200px; height: 720px; }

  .panel { position: absolute; background: var(--board); border: 1px solid var(--board-edge); overflow: hidden; }

  /* front face */
  .front { left: 50px; top: 50px; width: 360px; height: 620px; }
  .front .window {
    position: absolute; left: 40px; top: 100px; width: 280px; height: 270px;
    background: linear-gradient(135deg, #6f8a4a 0%, #b58a86 30%, #a7797a 55%, #9cbf6a 80%, #e8e1d2 100%);
    border: 2px solid #cfcac0;
  }
  .front .tagline {
    position: absolute; left: 24px; top: 490px; white-space: nowrap;
    font-family: "Parisienne", cursive; font-size: 24px; line-height: 30px; color: var(--red);
  }
  .front .band {
    position: absolute; left: 0; right: 0; bottom: 0; height: 90px; background: var(--red);
    color: var(--white); font-family: "Roboto Condensed", sans-serif; font-style: italic; font-weight: 700;
    font-size: 19px; line-height: 1.3; text-align: center; padding-top: 21px; letter-spacing: .3px;
  }

  .logo-badge {
    position: absolute; display: flex; align-items: center; justify-content: center; text-align: center;
    border: 2px solid var(--red); border-radius: 50%; background: var(--white);
    font-family: "Cormorant Garamond", serif; font-weight: 600; color: var(--red); line-height: 1.15;
  }
  .front .logo-badge { left: 214px; top: 378px; width: 108px; height: 108px; font-size: 11.5px; }

  /* side triangles */
  .side { position: absolute; }
  .side-left { left: 410px; top: 50px; width: 200px; height: 620px; }
  .side-right { left: 930px; top: 50px; width: 220px; height: 620px; }

  /* back face */
  .back { left: 690px; top: 50px; width: 240px; height: 620px; }
  .back .stripe { position: absolute; left: 90px; top: 0; width: 50px; height: 330px; background: var(--red); }
  .back .logo-badge { left: 60px; top: 300px; width: 110px; height: 110px; font-size: 11px; }
  .back .allergens {
    position: absolute; left: 14px; right: 14px; top: 436px;
    font-family: "Roboto Condensed", sans-serif; font-weight: 700; font-size: 7.5px; color: var(--ink);
    text-align: center; line-height: 1.4; white-space: nowrap;
  }
  .back .address {
    position: absolute; left: 28px; right: 28px; top: 486px; background: var(--white);
    font-family: "Roboto Condensed", sans-serif; font-weight: 700; text-align: center; white-space: nowrap;
  }
  .back .address-head { background: var(--red); color: var(--white); font-size: 10px; line-height: 1.5; padding: 8px 4px; }
  .back .address-mail { color: var(--red); font-size: 9px; padding: 9px 2px; }
  .corner-photo { position: absolute; border-radius: 6px; }
  .corner-milk { left: 0; top: 345px; width: 40px; height: 75px; background: linear-gradient(#ffffff, #e4e4e4); }
  .corner-wheat { right: 0; top: 290px; width: 50px; height: 135px; background: linear-gradient(#e2c48d, #b58a4f); }
  .corner-nuts { left: 0; top: 578px; width: 40px; height: 38px; background: linear-gradient(#c9a27a, #8e6440); }
  .corner-veg { right: 0; top: 578px; width: 50px; height: 38px; background: linear-gradient(#9fd36a, #d7c04a); }
</style>
</head>
<body>
<main class="canvas">

  <section class="panel front">
    <div class="window" role="img" aria-label="Window showing a ham, cheese and lettuce sandwich"></div>
    <div class="logo-badge">BRIGHT MEADOW<br>PANTRY<br>Hawks</div>
    <p class="tagline">Freshly Handmade Sandwiches</p>
    <div class="band">EAT ON DAY OF PURCHASE<br>KEEP REFRIGERATED BELOW 5°C</div>
  </section>

  <svg class="side side-left" viewBox="0 0 200 620">
    <defs>
      <linearGradient id="vegLeft" x1="0" y1="0" x2="1" y2="1">
        <stop offset="0" stop-color="#f1dd82"/>
        <stop offset="0.35" stop-color="#6fb43f"/>
        <stop offset="0.7" stop-color="#d9433a"/>
        <stop offset="1" stop-color="#f3c23a"/>
      </linearGradient>
    </defs>
    <polygon points="0,620 200,620 200,0" fill="#ecebe8" stroke="#d6d4cf"/>
    <polygon points="30,620 200,620 200,130" fill="url(#vegLeft)" role="img" aria-label="Fresh salad: lettuce, cucumber, tomato, peppers, olives, onion and cheese"/>
  </svg>

  <section class="panel back">
    <div class="stripe"></div>
    <div class="logo-badge">BRIGHT MEADOW<br>PANTRY<br>Hawks</div>
    <div class="corner-photo corner-milk" role="img" aria-label="Milk splash"></div>
    <div class="corner-photo corner-wheat" role="img" aria-label="Wheat ears"></div>
    <div class="corner-photo corner-nuts" role="img" aria-label="Mixed nuts"></div>
    <div class="corner-photo corner-veg" role="img" aria-label="Celery and soybeans"></div>
    <p class="allergens">MAY CONTAINS LUPIN, MOLLUSCS, MILK, BARLEY, SESAME SEEDS,<br>CRUSTACEANS, FISH, SULPHITES, SOYA, CELLERY &amp; NUTS</p>
    <div class="address">
      <div class="address-head">BRIGHT MEADOW PANTRY HAWKS LTD<br>UNIT 4 LARK LANE HK3 9QT</div>
      <div class="address-mail">HELLO@BRIGHTMEADOWPANTRY.EXAMPLE</div>
    </div>
  </section>

  <svg class="side side-right" viewBox="0 0 220 620">
    <defs>
      <linearGradient id="vegRight" x1="0" y1="0" x2="1" y2="1">
        <stop offset="0" stop-color="#f1dd82"/>
        <stop offset="0.35" stop-color="#6fb43f"/>
        <stop offset="0.7" stop-color="#d9433a"/>
        <stop offset="1" stop-color="#f3c23a"/>
      </linearGradient>
    </defs>
    <polygon points="0,0 0,620 220,620" fill="#ecebe8" stroke="#d6d4cf"/>
    <polygon points="0,130 0,620 190,620" fill="url(#vegRight)" role="img" aria-label="Fresh salad: lettuce, cucumber, tomato, peppers, olives, onion and cheese"/>
  </svg>

</main>
</body>
</html>
```